I need the below text put into an illustration/high res image so I can print out and frame and give to my fiance. Can be simple but must look elegant. Idea is that the text can be written in the sand on the attached pics (let me know if you require more high res). Not precious on the dimensions but think no more than 90cm length or width. Can be smaller whatever you think works best. You can half long sentences if you think it will look better.
Update: some of you asked for a picture of us, not sure it works but have attached one
Marriage
Marriage isn’t for you.
You don’t marry to make yourself happy, you marry to make someone else happy.
More than that, your marriage isn’t for yourself, you’re marrying for a family.
Not just for the in-laws and all of that nonsense, but for your future children.
Who do you want to help you raise them?
Who do you want to influence them?
Marriage isn’t for you.
It’s not about you.
Marriage is about the person you married.

```html
<!DOCTYPE html>
<html lang="en">
<head>
<meta charset="utf-8">
<title>Marriage Isn't For You</title>
<link rel="stylesheet" href="https://fonts.googleapis.com/css2?family=Parisienne&display=swap">
<style>
  :root {
    --sky: #c9d6e3;
    --sky-light: #e4eaef;
    --sea: #a9b8c3;
    --surf: #d5dde2;
    --sand-wet: #bdb8b1;
    --sand: #b3aba1;
    --sand-deep: #a59c91;
    --glow: #ffffff;
    --portrait-a: #8f8a80;
    --portrait-b: #5d6670;
    --ink: #6e6760;
    --ink-highlight: rgba(255, 255, 255, 0.55);
    --ink-shade: rgba(60, 52, 45, 0.35);
    --rose-area: #a9a095;
  }

  html, body {
    margin: 0;
    padding: 0;
    width: 1200px;
    height: 795px;
    overflow: hidden;
    background: var(--sand);
  }

  .canvas {
    position: relative;
    width: 1200px;
    height: 795px;
    overflow: hidden;
  }

  .beach-scene {
    position: absolute;
    inset: 0;
    background:
      linear-gradient(160deg, rgba(214, 222, 228, 0.55) 0%, rgba(214, 222, 228, 0.35) 22%, rgba(0, 0, 0, 0) 40%),
      linear-gradient(to bottom,
        var(--sky-light) 0px,
        var(--sky) 45px,
        var(--sea) 70px,
        var(--surf) 100px,
        var(--sand-wet) 150px,
        var(--sand) 260px,
        var(--sand-deep) 100%);
  }

  .portrait-glow {
    position: absolute;
    left: 55px;
    top: 40px;
    width: 560px;
    height: 460px;
    border-radius: 50%;
    background: radial-gradient(ellipse at center,
      rgba(255, 255, 255, 0.9) 60%,
      rgba(255, 255, 255, 0.5) 72%,
      rgba(255, 255, 255, 0) 80%);
  }

  .portrait {
    position: absolute;
    left: 80px;
    top: 40px;
    width: 505px;
    height: 440px;
    border-radius: 50%;
    background: radial-gradient(ellipse at 45% 45%, var(--portrait-a) 0%, var(--portrait-b) 85%);
    box-shadow: 0 0 22px 14px var(--glow);
  }

  .rose {
    position: absolute;
    left: 412px;
    top: 645px;
    width: 180px;
    height: 78px;
    border-radius: 40px;
    background: radial-gradient(ellipse at 30% 40%, var(--rose-area) 0%, rgba(169, 160, 149, 0) 75%);
  }

  .sand-writing {
    font-family: "Parisienne", cursive;
    color: var(--ink);
    text-shadow: 0 1px 0 var(--ink-highlight), 0 -1px 0 var(--ink-shade);
    margin: 0;
  }

  .verse {
    position: absolute;
    left: 650px;
    top: 135px;
    width: 550px;
    text-align: center;
    font-size: 21px;
    line-height: 33px;
  }

  .verse p {
    margin: 0 0 30px;
  }

  .verse p.tight {
    margin-bottom: 36px;
  }

  .closing {
    position: absolute;
    left: 75px;
    top: 566px;
    width: 520px;
    font-size: 28px;
    line-height: 40px;
    white-space: nowrap;
  }
</style>
</head>
<body>
  <main class="canvas">
    <div class="beach-scene" role="img" aria-label="Beach at low tide with waves, distant headland and pale sky"></div>

    <div class="portrait-glow"></div>
    <div class="portrait" role="img" aria-label="Oval portrait of the engaged couple embracing on the beach"></div>

    <div class="verse sand-writing">
      <p>Marriage isn’t for you.</p>
      <p>You don’t marry to make yourself happy,<br>you marry to make someone else happy.</p>
      <p>More than that, your marriage isn’t for yourself,<br>you’re marrying for a family.</p>
      <p>Not just for the in-laws and all of that nonsense,<br>but for your future children.</p>
      <p class="tight">Who do you want to help you raise them?</p>
      <p class="tight">Who do you want to influence them?</p>
      <p class="tight">Marriage isn’t for you.</p>
      <p>It’s not about you.</p>
    </div>

    <p class="closing sand-writing">Marriage is about the person you married.</p>

    <div class="rose" role="img" aria-label="A single white rose lying in the sand"></div>
  </main>
</body>
</html>
```